依頼詳細
ポスティング用のチラシです。
思わず手に取って見たくなるようなデザインとキャッチャーなコピーを
ご提案ください。

原稿にイラストを入れましたが、写真でも構いません。
また、全体のレイアウトも自由に変更頂いて構いません。

尚、コンペで表面が決まりましたら、裏面に着手していただきますので、
ご承知おきください。

それではご提案お待ちしております。
何卒よろしくお願い申し上げます。

記載項目
原稿にまとめました
サイズ
A4
ページ数
両面
希望イメージ
シンプル 複雑
単色 カラフル
暗い 明るい
日常 高級
遊び心 厳粛
未来的 伝統的
女性的 男性的
希望する色
納品ファイル
• イラストレーター形式 (.ai)
補足説明
お世話様でございます。
どれも素晴らしいご提案、誠にありがとうございました。
検討させていただきますので、決定までにしばらくお時間くださいませ。
宜しくお願い申し上げます。
■ 選んだ理由

インパクトのあるアイキャッチ(イラスト・コピー)と、非常に分かり易くまとめて頂いた所が
ポイントです。

■ 提案者全員のお礼・コメント

この度は素晴らしい作品をご提案頂きまして、誠にありがとうございました。
また機会を作りますので、今後ともよろしくお願い申し上げます。

```html
<!DOCTYPE html>
<html lang="ja">
<head>
<meta charset="utf-8">
<title>めがねのミルアイ 出張サービスのご案内</title>
<link rel="stylesheet" href="https://fonts.googleapis.com/css2?family=Noto+Sans+JP:wght@400;500;700;900&display=swap">
<style>
:root{
  --blue:#1d5fb8;
  --red:#e5141f;
  --orange:#f28a00;
  --navy:#1c2b4c;
  --ink:#1e1e1e;
  --cream:#fbf0d9;
  --cream-line:#e8b96a;
  --paper:#ffffff;
}
*{margin:0;padding:0;box-sizing:border-box}
html,body{width:846px;height:1200px;overflow:hidden;background:var(--paper)}
body{font-family:"Noto Sans JP",sans-serif;color:var(--ink);position:relative}
.flyer{position:relative;width:846px;height:1200px;overflow:hidden;background:var(--paper)}
.abs{position:absolute}

.hero-photo{left:430px;top:0;width:416px;height:350px;background:linear-gradient(160deg,#e9e6e2 0%,#cfc9c2 60%,#b8b1a8 100%)}
.headline{left:28px;top:18px;font-weight:900;color:var(--blue);line-height:1;letter-spacing:1px}
.headline .big{font-size:78px}
.headline .small{font-size:42px}
.but-badge{left:30px;top:118px;width:92px;height:92px;border-radius:50%;background:var(--blue);color:#fff;font-weight:900;font-size:34px;display:flex;align-items:center;justify-content:center}
.worry{left:140px;top:122px;font-weight:900;font-size:34px;line-height:1.3}
.bubble{left:612px;top:272px;font-size:16px;font-weight:500;line-height:1.3;background:rgba(255,255,255,.85);padding:6px 10px;border-radius:18px}
.to-you{left:30px;top:250px;font-weight:900;font-size:58px;letter-spacing:2px}

.free-list{left:30px;top:344px;width:270px;border:4px solid var(--red);padding:8px 14px;background:#fff}
.free-list li{list-style:none;font-weight:900;font-size:36px;color:var(--red);line-height:1.2}
.free-word{left:318px;top:352px;font-weight:900;font-size:118px;color:var(--red);letter-spacing:-2px;line-height:1}

.visit-band{left:0;top:500px;width:846px;height:92px;background:var(--orange)}
.visit-text{left:150px;top:506px;color:#fff;font-weight:900;font-size:30px;line-height:1.35;text-align:center;width:530px;white-space:nowrap}
.visit-van{left:704px;top:514px;width:108px;height:60px;border-radius:10px;background:#fff}
.visit-arrow{left:393px;top:590px}

.steps{left:18px;top:634px;width:556px;display:flex;align-items:flex-start}
.step{width:160px}
.step-photo{height:150px}
.step-photo.car{background:linear-gradient(150deg,#eef0f3,#a9b3bd)}
.step-photo.exam{background:linear-gradient(150deg,#5b6471,#2d333c)}
.step-photo.frames{background:linear-gradient(150deg,#eceae6,#b5aea6)}
.step-caption{background:var(--navy);color:#fff;font-weight:700;font-size:18px;line-height:1.3;text-align:center;padding:8px 6px;height:78px;display:flex;align-items:center;justify-content:center}
.step-caption.compact{font-size:14px;line-height:1.4}
.step-arrow{width:38px;display:flex;justify-content:center;padding-top:62px}
.delivery{left:588px;top:634px;width:240px}
.delivery-photo{height:150px;background:linear-gradient(150deg,#c8d6a8,#7e9366)}
.delivery-caption{background:#fff;border:3px solid var(--navy);color:var(--navy);font-weight:900;font-size:19px;line-height:1.35;text-align:center;padding:8px 4px}

.mascot{left:28px;top:900px;width:140px;height:96px;border-radius:8px;background:linear-gradient(180deg,#f2a43a,#c9731a)}
.company{left:182px;top:896px;font-weight:900;font-size:34px;line-height:1.2}
.address{left:420px;top:980px;font-size:15px;font-weight:500}
.phone-row{left:28px;top:1020px;display:flex;align-items:center;gap:10px}
.phone-mark{width:44px;height:44px;border-radius:50%;background:#2a9b3a}
.phone-num{font-weight:900;font-size:44px;color:var(--red);letter-spacing:1px}
.consult{left:24px;top:1090px;width:130px;font-weight:700;font-size:14px;color:var(--blue);line-height:1.45}
.safety-title{left:268px;top:1074px;font-weight:900;font-size:17px;color:var(--red)}
.safety-icons{left:164px;top:1104px;display:flex;gap:8px}
.safety-icons span{width:50px;height:50px;border-radius:6px;background:var(--blue)}

.voices{left:560px;top:900px;width:268px;height:288px;background:var(--cream);border:2px solid var(--cream-line);border-radius:8px;padding:12px 14px}
.voices h2{display:inline-block;background:var(--orange);color:#fff;font-size:17px;font-weight:900;padding:2px 12px;border-radius:14px;margin-bottom:10px}
.voice{font-size:12.5px;line-height:1.5;margin-bottom:10px}
.voice .who{font-weight:700;color:var(--orange)}
</style>
</head>
<body>
<main class="flyer">
  <div class="abs hero-photo" role="img" aria-label="眼鏡を持ち上げて見づらそうに目を細める年配の男性の写真"></div>
  <h1 class="abs headline"><span class="big">メガネ</span><span class="small">が欲しい…</span></h1>
  <div class="abs but-badge">でも</div>
  <p class="abs worry">新型コロナウイルスが<br>不安でお店に<br>いけない…。</p>
  <p class="abs bubble">見づらく<br>なったなぁ。</p>
  <p class="abs to-you">そんなあなたへ</p>

  <ul class="abs free-list">
    <li>視力測定</li>
    <li>超音波洗浄</li>
    <li>ネジ・調整</li>
  </ul>
  <p class="abs free-word">無料!!!</p>

  <div class="abs visit-band"></div>
  <p class="abs visit-text">お店に行かなくても大丈夫！<br>専用車でご自宅までうかがいます！</p>
  <div class="abs visit-van" role="img" aria-label="出張用の車のアイコン"></div>
  <svg class="abs visit-arrow" width="60" height="30" viewBox="0 0 60 30"><polygon points="0,0 60,0 30,30" fill="var(--orange)"/></svg>

  <section class="abs steps">
    <div class="step">
      <div class="step-photo car" role="img" aria-label="自宅前に停まった視力測定車の写真"></div>
      <p class="step-caption">視力測定車で<br>ご自宅に到着</p>
    </div>
    <div class="step-arrow"><svg width="22" height="30" viewBox="0 0 22 30"><polygon points="0,0 22,15 0,30" fill="var(--navy)"/></svg></div>
    <div class="step">
      <div class="step-photo exam" role="img" aria-label="車内の視力検査機器の写真"></div>
      <p class="step-caption">車内で<br>視力検査</p>
    </div>
    <div class="step-arrow"><svg width="22" height="30" viewBox="0 0 22 30"><polygon points="0,0 22,15 0,30" fill="var(--navy)"/></svg></div>
    <div class="step">
      <div class="step-photo frames" role="img" aria-label="並べられた眼鏡フレームの写真"></div>
      <p class="step-caption compact">レンズ・フレームを<br>お選びいただきます</p>
    </div>
  </section>
  <section class="abs delivery">
    <div class="delivery-photo" role="img" aria-label="眼鏡を受け取り笑顔の年配の夫婦の写真"></div>
    <p class="delivery-caption">ご注文後、<br>会社やご自宅まで<br>お届けします！</p>
  </section>

  <div class="abs mascot" role="img" aria-label="店のマスコットのダックスフントのイラスト"></div>
  <p class="abs company">株式会社 ミルアイ<br>めがねのミルアイ</p>
  <p class="abs address">長野市若葉町 112</p>
  <div class="abs phone-row"><span class="phone-mark"></span><span class="phone-num">0120-00-4417</span></div>
  <p class="abs consult">メガネのことなら<br>何でもご相談<br>ください！</p>
  <p class="abs safety-title">感染対策強化中!!</p>
  <div class="abs safety-icons"><span></span><span></span><span></span><span></span><span></span></div>

  <aside class="abs voices">
    <h2>お客様の声</h2>
    <p class="voice"><span class="who">長野市 A様 60代 女性</span><br>外出が不安でしたが、自宅まで来ていただき安心して眼鏡を作れました。丁寧な説明もうれしかったです。</p>
    <p class="voice"><span class="who">長野市 B様 70代 男性</span><br>足が悪く店に行けず困っていました。車内でしっかり検査してもらい、よく見える眼鏡が届きました。</p>
  </aside>
</main>
</body>
</html>
```